Orvik Lines website

i'm looking for a promotional website for my business.
we provide Rope Access, Work at Height & Difficult Access services.
we treat water leak into buildings, external renovation of buildings, windows cleaning, confined spaces services and practically jobs in which the access is difficult.
here are examples of web site i like :
http://www.layoutbazaar.example/wordpress-themes/51872.html
http://www.layoutbazaar.example/joomla-templates/51294.html

private people, commercial household chiefs, maintenance managers

Business

• - mobile friendly
- frindlo redirection
- 5 tabs
- one more customizable page - so i can add a photo and a description of the service corresponding (for now i offer 7 different services)
- contact us on each page with no redirection
- we are offering 7 different services
the website will be published in Israel which means right to left or centered for english option in the future. (logo on left hand corner)

- no flash
- should be future customisable - for future
• - a space for a slogan
- non scrollable
- photos on the landing page + redirection to gallery (photos and short films)
- 3 dynamic banners with short description of the theme of each, clicking on the banner after it opened will redirect to it's corresponding page.

```html
<!DOCTYPE html>
<html lang="en">
<head>
<meta charset="utf-8">
<title>Orvik Lines</title>
<link rel="stylesheet" href="https://fonts.googleapis.com/css2?family=Ubuntu:wght@400;500;700&family=Arimo:ital,wght@0,400;0,700;1,400&display=swap">
<style>
:root{
  --ink:#2b2b2b;
  --text:#444;
  --muted:#777;
  --header-bg:#e4e4e4;
  --pill:#c9c9c9;
  --dark:#3d3d3d;
  --dark-2:#353535;
  --band-text:#f2f2f2;
  --footer-bg:#efefef;
  --bottom:#6b6b6b;
  --sky:#6f95c9;
  --line:#cfcfcf;
}
*{box-sizing:border-box;margin:0;padding:0}
html,body{width:823px;height:1200px;overflow:hidden;background:#fff}
body{position:relative;font-family:"Arimo",Arial,sans-serif;color:var(--text)}
.abs{position:absolute}

/* header */
.site-header{left:0;top:0;width:823px;height:104px;background:linear-gradient(#ededed,#dcdcdc);border-top:2px solid #bdbdbd}
.brand{left:92px;top:14px;display:flex;align-items:center;gap:14px}
.brand-mark{width:62px;height:62px;border-radius:50%;background:var(--ink)}
.brand-name{font-family:"Ubuntu",sans-serif;font-size:19px;font-weight:500;color:var(--ink);margin-top:34px}
.topbar{left:464px;top:0;width:268px;height:26px;background:var(--pill);border-radius:0 0 22px 22px;display:flex;align-items:center;justify-content:center;gap:20px;font-family:"Ubuntu",sans-serif}
.topbar .call{font-size:12px;color:#333;font-weight:500}
.topbar .call b{color:#fff;font-weight:500}
.topbar .lang{font-size:7.5px;color:#222;font-weight:700}
.topbar .lang span{color:#fff;margin-left:4px}
.main-nav{left:375px;top:69px;display:flex;align-items:center;font-family:"Ubuntu",sans-serif;font-size:9.5px;font-weight:500;color:#333}
.main-nav a{color:inherit;text-decoration:none;margin-right:31px}
.main-nav a.active{background:#2f2f2f;color:#fff;border-radius:12px;padding:5px 15px;margin-right:20px}

/* hero */
.hero{left:0;top:104px;width:823px;height:316px;background:linear-gradient(120deg,#4f78b3 0%,#8eb0db 45%,#bcd1ea 70%,#7a9ccc 100%)}
.hero-tagline{left:440px;top:198px;font-family:"Ubuntu",sans-serif;font-weight:700;font-size:23px;line-height:31px;color:#fff;text-shadow:0 1px 3px rgba(0,0,0,.6)}
.hero-dots{left:666px;top:392px;display:flex;gap:6px}
.hero-dots i{width:13px;height:13px;border-radius:50%;background:#4f6378;display:block}
.hero-dots i.on{background:#2a2a2a}

/* services */
.services{left:0;top:420px;width:823px;height:258px;background:var(--dark)}
.service{top:20px;width:130px;margin-left:-65px;display:flex;flex-direction:column;align-items:center;color:var(--band-text)}
.service h3{font-family:"Ubuntu",sans-serif;font-weight:500;font-size:13px;line-height:16px;text-align:center;letter-spacing:.6px;height:60px;display:flex;align-items:center}
.service .thumb{width:102px;height:102px;border-radius:50%;border:3px solid #555;margin-top:2px}
.service .more{font-size:10px;color:#ccc;margin-top:24px;letter-spacing:.3px}
.service svg{margin-top:8px}

/* content */
.col{top:700px;width:198px}
.col h2{font-family:"Ubuntu",sans-serif;font-weight:500;font-size:16px;color:#3a3a3a;letter-spacing:.3px}
.col .pic{width:198px;height:106px;margin-top:12px;border:1px solid #ccc}
.col p{font-size:8.4px;line-height:15.8px;margin-top:14px;color:var(--text)}
.col p strong{color:#222}
.readmore{font-size:8.6px;font-weight:700;color:#222;letter-spacing:.3px}
.quote{font-style:italic;font-size:8.4px;line-height:15.8px;color:#555}
.quote-by{text-align:right;font-style:italic;font-size:8.4px;line-height:12px;color:#666}
.avatar{width:54px;height:47px;border:1px solid #ccc}

/* footer */
.footer{left:0;top:990px;width:823px;height:170px;background:var(--footer-bg)}
.footer h2{font-family:"Ubuntu",sans-serif;font-weight:500;font-size:16px;color:#3a3a3a;letter-spacing:.3px}
.vline{width:1px;top:1010px;height:124px;background:var(--line)}
.date{left:90px;top:1038px;width:48px;height:48px;border-radius:50%;background:#9a9a9a;color:#fff;font-family:Georgia,serif;text-align:center;line-height:1}
.date small{display:block;font-size:10px;margin-top:7px}
.date b{display:block;font-size:19px;font-weight:400}
.fsmall{font-size:8.4px;line-height:13.6px;color:#444}
.contact-row{display:flex;font-size:8.4px;color:#222}
.social{display:flex;align-items:center;gap:7px;font-size:8.4px;color:#222}
.social i{display:block;width:19px;height:19px;border-radius:3px}
.bottom-bar{left:0;top:1160px;width:823px;height:40px;background:var(--bottom);color:#eee;font-size:7px;text-align:center;line-height:40px}
</style>
</head>
<body>

<header class="site-header abs">
  <div class="topbar abs">
    <span class="call">Call Us: <b>1 800 555 0142</b></span>
    <span class="lang">Language : <span>Israel ▾</span></span>
  </div>
</header>
<div class="brand abs"><div class="brand-mark"></div><span class="brand-name">orvik lines</span></div>
<nav class="main-nav abs">
  <a class="active" href="#">Home</a><a href="#">About Us</a><a href="#">Services</a><a href="#">Testimonials</a><a href="#">Contact Us</a>
</nav>

<section class="hero abs" role="img" aria-label="Rope access technician cleaning a glass facade against a blue sky"></section>
<div class="hero-tagline abs">We provide Rope Access,<br>Work at Height &amp; Difficult<br>Access Services....</div>
<div class="hero-dots abs"><i class="on"></i><i></i><i></i><i></i></div>

<section class="services abs">
  <div class="service abs" style="left:144px"><h3>Rope<br>Access</h3><div class="thumb" role="img" aria-label="Climber hanging on ropes" style="background:radial-gradient(#4d8fd1,#1f5fb0)"></div><span class="more">Learn More</span><svg width="15" height="15" viewBox="0 0 15 15"><circle cx="7.5" cy="7.5" r="6.5" fill="none" stroke="#ddd" stroke-width="1.2"/><path d="M6 4.5l3.5 3-3.5 3z" fill="#ddd"/></svg></div>
  <div class="service abs" style="left:278px"><h3>Work at<br>Height &amp;<br>Difficult Access</h3><div class="thumb" role="img" aria-label="Worker in helmet at height" style="background:radial-gradient(#7fa6d4,#3c64a8)"></div><span class="more">Learn More</span><svg width="15" height="15" viewBox="0 0 15 15"><circle cx="7.5" cy="7.5" r="6.5" fill="none" stroke="#ddd" stroke-width="1.2"/><path d="M6 4.5l3.5 3-3.5 3z" fill="#ddd"/></svg></div>
  <div class="service abs" style="left:413px"><h3>Treat<br>Water Leak<br>into Buildings</h3><div class="thumb" role="img" aria-label="Sealing a roof surface against leaks" style="background:radial-gradient(#d99a73,#7c7a76)"></div><span class="more">Learn More</span><svg width="15" height="15" viewBox="0 0 15 15"><circle cx="7.5" cy="7.5" r="6.5" fill="none" stroke="#ddd" stroke-width="1.2"/><path d="M6 4.5l3.5 3-3.5 3z" fill="#ddd"/></svg></div>
  <div class="service abs" style="left:546px"><h3>External<br>Renovation of<br>Buildings</h3><div class="thumb" role="img" aria-label="Worker in high-visibility vest renovating a wall" style="background:radial-gradient(#c7c7c0,#8d9a55)"></div><span class="more">Learn More</span><svg width="15" height="15" viewBox="0 0 15 15"><circle cx="7.5" cy="7.5" r="6.5" fill="none" stroke="#ddd" stroke-width="1.2"/><path d="M6 4.5l3.5 3-3.5 3z" fill="#ddd"/></svg></div>
  <div class="service abs" style="left:681px"><h3>Windows<br>Cleaning</h3><div class="thumb" role="img" aria-label="Window cleaner with squeegee" style="background:radial-gradient(#a8c2de,#6f7f93)"></div><span class="more">Learn More</span><svg width="15" height="15" viewBox="0 0 15 15"><circle cx="7.5" cy="7.5" r="6.5" fill="none" stroke="#ddd" stroke-width="1.2"/><path d="M6 4.5l3.5 3-3.5 3z" fill="#ddd"/></svg></div>
</section>

<section class="col abs" style="left:90px">
  <h2>Welcome to Our Site!</h2>
  <div class="pic" role="img" aria-label="Rope worker on a rooftop above a hazy city" style="background:linear-gradient(#8d8a86,#c4ad91)"></div>
  <p><strong>Donec accumsan malesuada orci. Donec sit amet eros. Lorem ipsum dolor sit amet.</strong><br>Praesent vestibulum molestie lacus. Aenean nonummy hendrerit mauris. Phasellus porta. Fusce suscipit varius mi. Cum sociis natoque penatibus et magnis dis parturient montes, nascetur ridiculus mus.</p>
</section>
<a class="readmore abs" style="left:90px;top:964px">READ MORE &gt;&gt;</a>

<section class="col abs" style="left:309px">
  <h2>What We Do</h2>
  <div class="pic" role="img" aria-label="Worker's harness and tool belt close up" style="background:linear-gradient(100deg,#5a5a5a,#9a9a9a 60%,#c8c8c8)"></div>
  <p>Praesent vestibulum molestie lacus. Aenean nonummy hendrerit mauris. Phasellus porta. Fusce suscipit varius mi. Cum sociis natoque penatibus et magnis dis parturient montes, nascetur ridiculus mus. Phasellus porta. Fusce suscipit varius mi. Cum sociis natoque penati­bus.</p>
</section>
<a class="readmore abs" style="left:309px;top:964px">READ MORE &gt;&gt;</a>

<section class="col abs" style="left:538px;width:196px">
  <h2>Testimonials</h2>
</section>
<p class="quote abs" style="left:538px;top:723px;width:196px">Cum sociis natoque penatibus et magnis dis parturient montes, nascetur ridiculus mus...</p>
<div class="quote-by abs" style="left:600px;top:786px;width:72px">By<br>Tomas Reld</div>
<div class="avatar abs" role="img" aria-label="Client portrait" style="left:679px;top:767px;background:linear-gradient(#e6e6e6,#b5b5b5)"></div>
<div class="abs" style="left:538px;top:830px;width:196px;height:1px;background:var(--line)"></div>
<p class="quote abs" style="left:538px;top:839px;width:196px">Cum sociis natoque penatibus et magnis dis parturient montes, nascetur ridiculus mus...</p>
<div class="quote-by abs" style="left:600px;top:902px;width:72px">By<br>Tomas Reld</div>
<div class="avatar abs" role="img" aria-label="Client portrait" style="left:679px;top:883px;background:linear-gradient(#f0f0f0,#c2c7cf)"></div>
<a class="readmore abs" style="left:537px;top:966px">READ ALL TESTIMONIALS &gt;&gt;</a>

<footer class="footer abs"></footer>
<div class="vline abs" style="left:322px"></div>
<div class="vline abs" style="left:526px"></div>

<h2 class="abs" style="left:90px;top:1006px;font-family:'Ubuntu',sans-serif;font-weight:500;font-size:16px;color:#3a3a3a">Latest News</h2>
<div class="date abs"><small>Apr</small><b>15</b></div>
<div class="abs fsmall" style="left:145px;top:1036px;width:160px"><strong style="color:#222">Donec accumsan malesuada orci. Donec sit amet eros.</strong><br>Praesent vestibulum molestie lacus. Aenean nonummy hendrerit mauris....</div>
<a class="readmore abs" style="left:90px;top:1127px">READ ALL NEWS &gt;&gt;</a>

<h2 class="abs" style="left:351px;top:1006px;font-family:'Ubuntu',sans-serif;font-weight:500;font-size:16px;color:#3a3a3a">Contact Us</h2>
<div class="abs fsmall" style="left:351px;top:1036px"><strong style="color:#222">Orvik Lines</strong><br>42 Harbour Lane,<br>Leith, EH6 7QT.</div>
<div class="contact-row abs" style="left:351px;top:1082px"><span style="width:75px">Telephone:</span>+1 800 555 0142</div>
<div class="contact-row abs" style="left:351px;top:1100px"><span style="width:75px">FAX:</span>+1 800 555 0177</div>
<div class="contact-row abs" style="left:351px;top:1117px"><span style="width:58px">E-mail:</span>info@orviklines.example</div>

<h2 class="abs" style="left:557px;top:1006px;font-family:'Ubuntu',sans-serif;font-weight:500;font-size:16px;color:#3a3a3a">Connect Us</h2>
<div class="social abs" style="left:558px;top:1033px"><i style="background:#3b5a97"></i>Frindlo</div>
<div class="social abs" style="left:558px;top:1060px"><i style="background:#45a8d6"></i>Chirpline</div>
<div class="social abs" style="left:558px;top:1086px"><i style="background:#1f7bb5"></i>Netlink</div>
<div class="social abs" style="left:558px;top:1113px"><i style="background:#e6812f"></i>Rss Feed</div>

<div class="bottom-bar abs">Copyright © 2013. Orvik Lines.All Right Reserved</div>

</body>
</html>
```